Patient Engagement Solution

We need an attractive and easy-to-use GUI for patients and clinicians, which includes screens and icons. The application has been named Quorvix. I have our corporate logo attached as well.
I have attached the screens that the developer has used to create the solution, but we all know they miss the target when it comes to the creative stuff.
If it helps, I can supply some competitor's screens as a guide - please let me know.

Target Market(s)

Patients and Clinicians

Industry/Entity Type

Healthcare/Hospitals

Font styles to use
Other font styles liked:
• Easy to Read

Requirements
Must have
• Attractive, easy to use graphical user interface. Screen size is usually 22" 16:9
Nice to have
• Inviting and interesting look
Should not have
• Complicated hard to navigate screens

```html
<!DOCTYPE html>
<html lang="en">
<head>
<meta charset="utf-8">
<title>Quorvix – Home</title>
<link href="https://fonts.googleapis.com/css2?family=ABeeZee&family=Nunito:wght@600;800&display=swap" rel="stylesheet">
<style>
  :root {
    --bar: #1e1e1e;
    --nav: rgba(30, 34, 38, 0.72);
    --white: #ffffff;
    --accent: #e8232a;
    --deep: #06121c;
    --blue: #1f6fa8;
    --orange: #e0582a;
  }
  * { box-sizing: border-box; margin: 0; padding: 0; }
  html, body { width: 1200px; height: 675px; overflow: hidden; background: var(--deep); }
  .screen { position: relative; width: 1200px; height: 675px; overflow: hidden; font-family: "Nunito", sans-serif; color: var(--white); }
  .backdrop {
    position: absolute; inset: 62px 0 0 0;
    background:
      radial-gradient(ellipse 35% 45% at 78% 50%, rgba(232, 96, 40, 0.85), transparent 70%),
      radial-gradient(ellipse 30% 40% at 40% 25%, rgba(40, 140, 200, 0.75), transparent 70%),
      radial-gradient(ellipse 25% 35% at 20% 70%, rgba(30, 110, 170, 0.6), transparent 70%),
      radial-gradient(ellipse 20% 25% at 35% 12%, rgba(230, 70, 50, 0.7), transparent 70%),
      linear-gradient(90deg, #07182a 0%, #0c2a44 45%, #3a1c1c 70%, #1a0f12 100%);
  }
  .top-bar { position: absolute; top: 0; left: 0; width: 1200px; height: 62px; background: var(--bar); display: flex; align-items: center; justify-content: center; }
  .brand-name { font-family: "Nunito", sans-serif; font-weight: 800; font-size: 24px; color: var(--white); letter-spacing: -0.3px; }
  .clock { position: absolute; top: 128px; left: 0; width: 100%; text-align: center; font-family: "ABeeZee", sans-serif; font-size: 90px; line-height: 1; letter-spacing: 2px; }
  .date { position: absolute; top: 226px; left: 0; width: 100%; text-align: center; font-family: "ABeeZee", sans-serif; font-size: 31px; letter-spacing: 0.5px; }
  .nav { position: absolute; left: 0; top: 523px; width: 1200px; height: 152px; background: var(--nav); }
  .nav-item { position: absolute; top: 40px; width: 160px; margin-left: -80px; text-align: center; }
  .nav-item svg { display: block; margin: 0 auto; width: 50px; height: 46px; }
  .nav-label { display: block; margin-top: 6px; font-size: 19px; font-weight: 600; line-height: 1; }
  .nav-item.is-active .nav-label { color: var(--accent); }
</style>
</head>
<body>
<div class="screen">
  <div class="backdrop" role="img" aria-label="Abstract background photograph of blue and orange ink clouds swirling in dark water"></div>

  <header class="top-bar"><span class="brand-name">Quorvix</span></header>

  <div class="clock">04:04</div>
  <div class="date">Friday 07 September 2023</div>

  <nav class="nav">
    <div class="nav-item is-active" style="left:79px">
      <svg viewBox="0 0 50 46"><path d="M25 2 L45 14 Q46 15 46 17 V40 Q46 44 42 44 H8 Q4 44 4 40 V17 Q4 15 5 14 Z" fill="#e8232a" stroke="#e8232a" stroke-width="2" stroke-linejoin="round"/><path d="M17 29 Q25 35 33 29" fill="none" stroke="#1e1e1e" stroke-width="3" stroke-linecap="round"/></svg>
      <span class="nav-label">Home</span>
    </div>
    <div class="nav-item" style="left:256px">
      <svg viewBox="0 0 50 46" fill="none" stroke="#fff" stroke-width="3.5"><rect x="2" y="4" width="46" height="32" rx="2"/><path d="M14 40 H36" stroke-width="4"/><path d="M8 16 A14 14 0 0 1 22 30 M8 22 A8 8 0 0 1 16 30"/><circle cx="9.5" cy="28.5" r="1.8" fill="#fff"/></svg>
      <span class="nav-label">Entertainment</span>
    </div>
    <div class="nav-item" style="left:436px">
      <svg viewBox="0 0 50 46" fill="none" stroke="#fff" stroke-width="3.2"><path d="M14 8 H36 Q44 8 46 22 Q48 38 42 38 Q38 38 34 31 H16 Q12 38 8 38 Q2 38 4 22 Q6 8 14 8 Z"/><path d="M15 16 V26 M10 21 H20"/><circle cx="33" cy="18" r="1.8" fill="#fff"/><circle cx="38" cy="22" r="1.8" fill="#fff"/><circle cx="30" cy="23" r="1.8" fill="#fff"/></svg>
      <span class="nav-label">Games</span>
    </div>
    <div class="nav-item" style="left:589px">
      <svg viewBox="0 0 50 46" fill="none" stroke="#fff" stroke-width="3.5" stroke-linejoin="round"><path d="M18 2 H32 V14 H44 V30 H32 V42 H18 V30 H6 V14 H18 Z"/><path d="M8 24 H18 L22 16 L27 30 L30 22 H42" stroke-width="3"/></svg>
      <span class="nav-label">My Care</span>
    </div>
    <div class="nav-item" style="left:763px">
      <svg viewBox="0 0 50 46" fill="none" stroke="#fff" stroke-width="3.5"><rect x="5" y="3" width="16" height="16"/><circle cx="37" cy="11" r="8"/><rect x="5" y="27" width="16" height="16"/><rect x="29" y="27" width="16" height="16"/></svg>
      <span class="nav-label">Application</span>
    </div>
    <div class="nav-item" style="left:944px">
      <svg viewBox="0 0 50 46" fill="none" stroke="#fff" stroke-width="2.8"><circle cx="15" cy="13" r="11"/><path d="M4 13 H26 M15 2 V24 M15 2 Q8 13 15 24 M15 2 Q22 13 15 24"/><path d="M9 44 L16 26 L23 44 M12 37 H20"/><path d="M28 24 H46 M37 20 V24 M30 29 H44 L38 34 M37 34 V44 Q37 46 33 45 M28 38 H46"/></svg>
      <span class="nav-label">Language</span>
    </div>
    <div class="nav-item" style="left:1111px">
      <svg viewBox="0 0 50 46" fill="none" stroke="#fff" stroke-width="4" stroke-linejoin="round"><path d="M21 3 H29 L30 9 L35 11 L40 7 L45 13 L41 18 L43 23 L48 24 V30 L43 31 L41 36 L44 41 L38 46 L33 42 L29 44 H21 L17 42 L12 46 L6 41 L9 36 L7 31 L2 30 V24 L7 23 L9 18 L5 13 L10 7 L15 11 L20 9 Z" transform="translate(0 -2) scale(1 0.98)"/><circle cx="25" cy="23" r="7"/></svg>
      <span class="nav-label">Settings</span>
    </div>
  </nav>
</div>
</body>
</html>
```